Northfield Builders Guild Business card

We are looking for a new business card design with photo included.
Our business is a nonprofit construction contractor membership organization. We offer business education, assist with business setup and licensing, provide safety training, and provide a member directory.
URL: www.brickwayguildnetwork.org
Color code:
CMYK: 0 cyan, 42 magenta, 100 yellow, 0 black for Print.
Hexidecimal: #FF9900
RGB: R 255; G 153; B 0

```html
<!DOCTYPE html>
<html lang="en">
<head>
<meta charset="utf-8">
<title>Northfield Builders Guild – Business Card</title>
<link href="https://fonts.googleapis.com/css2?family=Montserrat:wght@300;400;500;700;800;900&display=swap" rel="stylesheet">
<style>
  :root{
    --bg:#1b1b1b;
    --card-dark:#2e2e2e;
    --card-deep:#232323;
    --accent:#f6b21c;
    --ink:#1c1c1c;
    --photo-a:#2b3444;
    --photo-b:#161a22;
  }
  *{box-sizing:border-box;margin:0;padding:0}
  html,body{width:1200px;height:900px;overflow:hidden;background:var(--bg);font-family:"Montserrat",sans-serif}
  .card{position:absolute;left:120px;top:176px;width:960px;height:548px;background:linear-gradient(135deg,#363636 0%,var(--card-dark) 50%,var(--card-deep) 100%);overflow:hidden;box-shadow:0 20px 50px rgba(0,0,0,.6)}
  .card-shapes{position:absolute;inset:0}
  .photo-frame{position:absolute;left:250px;top:44px;width:270px;height:190px;border:7px solid var(--accent);border-radius:6px;background:var(--ink)}
  .photo{width:100%;height:100%;background:radial-gradient(circle at 55% 40%,var(--photo-a),var(--photo-b))}
  .name-block{position:absolute;left:40px;top:244px;color:var(--ink)}
  .name{font-weight:800;font-size:28px;letter-spacing:.5px;text-transform:uppercase;line-height:1.1}
  .role{font-weight:300;font-size:16px;letter-spacing:1px;text-transform:uppercase;margin-top:2px;color:var(--ink)}
  .brand{position:absolute;left:600px;top:168px;width:340px;color:var(--accent);font-weight:800;font-size:42px;line-height:1.04;text-transform:uppercase;letter-spacing:.5px}
  .contacts{position:absolute;list-style:none;color:var(--ink)}
  .contacts li{display:flex;align-items:center;gap:12px;height:36px;border-bottom:1px solid rgba(28,28,28,.55);font-size:16px;font-weight:500;white-space:nowrap}
  .contacts-main{left:320px;top:300px;width:250px}
  .contacts-web{left:600px;top:330px;width:330px}
  .icon{width:28px;height:24px;border-radius:4px;background:var(--ink);display:flex;align-items:center;justify-content:center;flex:none}
  .icon svg{width:15px;height:15px}
  .address{position:absolute;left:320px;top:414px;width:420px;color:var(--ink);font-size:15px;font-weight:500;line-height:30px;white-space:nowrap;border-bottom:1px solid rgba(28,28,28,.55)}
</style>
</head>
<body>
<section class="card" aria-label="Northfield Builders Guild business card">
  <svg class="card-shapes" width="960" height="548" viewBox="0 0 960 548" aria-hidden="true">
    <polygon points="330,0 620,0 700,120 680,120 610,14 330,14" fill="var(--accent)"/>
    <polygon points="0,215 545,215 580,320 960,320 960,505 0,505" fill="var(--accent)"/>
    <rect x="0" y="505" width="960" height="43" fill="var(--card-deep)"/>
  </svg>

  <div class="photo-frame"><div class="photo" role="img" aria-label="Portrait photo of the general manager"></div></div>

  <div class="name-block">
    <p class="name">Daniel Mercer</p>
    <p class="role">General Manager</p>
  </div>

  <p class="brand">Northfield Builders Guild</p>

  <ul class="contacts contacts-main">
    <li><span class="icon"><svg viewBox="0 0 16 16"><path d="M4 1l3 3-2 2c1 2 3 4 5 5l2-2 3 3-2 3C7 14 2 9 1 3z" fill="var(--accent)"/></svg></span>(555) 214-3087</li>
    <li><span class="icon"><svg viewBox="0 0 16 16"><rect x="4" y="1" width="8" height="14" rx="1.5" fill="none" stroke="var(--accent)" stroke-width="1.6"/><circle cx="8" cy="12.5" r="1" fill="var(--accent)"/></svg></span>555.380.1624</li>
    <li><span class="icon"><svg viewBox="0 0 16 16"><path d="M8 1a5 5 0 0 1 5 5c0 4-5 9-5 9S3 10 3 6a5 5 0 0 1 5-5z" fill="var(--accent)"/><circle cx="8" cy="6" r="2" fill="var(--ink)"/></svg></span>Northfield Builders Guild</li>
  </ul>
  <p class="address">4200 Larkspur Ave, Suite #210 Milbrook, OR 97000</p>

  <ul class="contacts contacts-web">
    <li><span class="icon"><svg viewBox="0 0 16 16"><circle cx="8" cy="8" r="6.5" fill="none" stroke="var(--accent)" stroke-width="1.4"/><ellipse cx="8" cy="8" rx="2.8" ry="6.5" fill="none" stroke="var(--accent)" stroke-width="1.2"/><line x1="1.5" y1="8" x2="14.5" y2="8" stroke="var(--accent)" stroke-width="1.2"/></svg></span>www.brickwayguildnetwork.org</li>
    <li><span class="icon"><svg viewBox="0 0 16 16"><rect x="1" y="3" width="14" height="10" rx="1" fill="var(--accent)"/><path d="M1.5 3.5L8 9l6.5-5.5" fill="none" stroke="var(--ink)" stroke-width="1.3"/></svg></span>support@brickwayguild.org</li>
  </ul>
</section>
</body>
</html>
```